Veterinary Business cards

Redesign Business Card

Information needed on Card:
Hours: Mon-Fri: 4pm -10PM; Sat- Sun- 10 AM- 5PM
Help@bayfernvet.com
www.bayfernvet.com
555-718-2946
4173 SE 19th Ave. okc, ok 73958
*No appointment necessary*

Optional:
Our tag line is "We're here when you need us" - If it fits on the cards.

```html
<!DOCTYPE html>
<html lang="en">
<head>
<meta charset="utf-8">
<title>Bayfern Urgent Care – Business Cards</title>
<link rel="stylesheet" href="https://fonts.googleapis.com/css2?family=Montserrat:ital,wght@0,400;0,500;0,700;1,400&display=swap">
<style>
  :root {
    --navy: #1b3a66;
    --orange: #d57a2a;
    --white: #ffffff;
    --page: #f7f7f7;
    --shadow: 0 6px 14px rgba(0,0,0,0.22);
  }
  * { margin: 0; padding: 0; box-sizing: border-box; }
  html, body { width: 800px; height: 1200px; overflow: hidden; }
  body {
    background: var(--page);
    font-family: "Montserrat", sans-serif;
    position: relative;
  }
  .card {
    position: absolute;
    left: 80px;
    width: 640px;
    height: 366px;
    overflow: hidden;
    box-shadow: var(--shadow);
  }
  .card--front { top: 190px; }
  .card--back { top: 644px; background: var(--navy); }
  .card-bg { position: absolute; inset: 0; width: 100%; height: 100%; }

  .brand { position: absolute; text-align: center; font-weight: 500; }
  .brand-name { display: block; font-size: 50px; letter-spacing: 4px; line-height: 1; }
  .brand-sub { display: block; font-size: 18px; letter-spacing: 7px; margin-top: 6px; line-height: 1; }

  .card--front .brand { left: 42px; top: 36px; width: 340px; color: var(--navy); }

  .contact-list {
    position: absolute; left: 44px; top: 190px;
    list-style: none; color: var(--white); font-size: 17px; font-weight: 400;
  }
  .contact-item { display: flex; align-items: flex-start; margin-bottom: 9px; line-height: 1.2; }
  .contact-icon { width: 13px; height: 13px; margin: 3px 10px 0 0; flex: none; fill: var(--orange); }

  .card--back .brand { left: 0; right: 0; top: 100px; color: var(--white); }
  .availability {
    position: absolute; left: 0; right: 0; top: 37px; text-align: center;
    color: var(--white); font-weight: 700; font-size: 15px; letter-spacing: 3.5px;
  }
  .web-address {
    position: absolute; left: 0; right: 0; top: 205px; text-align: center;
    color: var(--white); font-size: 16px;
  }
  .tagline {
    position: absolute; left: 0; right: 0; top: 290px; text-align: center;
    color: var(--white); font-style: italic; font-size: 20px; letter-spacing: 0.5px;
  }
</style>
</head>
<body>

<section class="card card--front">
  <svg class="card-bg" viewBox="0 0 929 532" preserveAspectRatio="none" aria-hidden="true">
    <rect width="929" height="532" fill="var(--white)"/>
    <path fill="var(--navy)" d="M0,170 C110,165 190,228 310,226 C430,224 520,172 640,172 C668,172 662,100 672,60 C682,20 695,0 695,0 L929,0 L929,340 C870,340 840,380 825,430 C810,480 800,510 785,532 L0,532 Z"/>
    <circle class="brand-disc" cx="733" cy="265" r="153" fill="var(--orange)"/>
  </svg>

  <div class="brand">
    <span class="brand-name">BAYFERN</span>
    <span class="brand-sub">URGENT CARE</span>
  </div>

  <ul class="contact-list">
    <li class="contact-item">
      <svg class="contact-icon" viewBox="0 0 16 16"><path d="M3.5 1 L6 1 L7 4.5 L5.3 6 C6.2 8 8 9.8 10 10.7 L11.5 9 L15 10 L15 12.5 C15 13.9 13.9 15 12.5 15 C6.7 15 1 9.3 1 3.5 C1 2.1 2.1 1 3.5 1 Z"/></svg>
      <span>555-718-2946</span>
    </li>
    <li class="contact-item">
      <svg class="contact-icon" viewBox="0 0 16 16"><path d="M8 0 C4.7 0 2.5 2.4 2.5 5.5 C2.5 9.5 8 16 8 16 C8 16 13.5 9.5 13.5 5.5 C13.5 2.4 11.3 0 8 0 Z M8 3.5 A2 2 0 1 1 8 7.5 A2 2 0 1 1 8 3.5 Z" fill-rule="evenodd"/></svg>
      <span>4173 SE 19th Ave. OKC, OK 73958</span>
    </li>
    <li class="contact-item">
      <svg class="contact-icon" viewBox="0 0 16 16"><path d="M0 3 L16 3 L16 13 L0 13 Z M1.5 4.5 L8 9 L14.5 4.5" fill-rule="evenodd"/><path d="M1 4 L8 9 L15 4" stroke="var(--navy)" stroke-width="1.5" fill="none"/></svg>
      <span>Help@bayfernvet.com</span>
    </li>
    <li class="contact-item">
      <svg class="contact-icon" viewBox="0 0 16 16"><path d="M1 3 L15 3 L15 15 L1 15 Z M2.5 6 L2.5 13.5 L13.5 13.5 L13.5 6 Z M4 1 L5.5 1 L5.5 4 L4 4 Z M10.5 1 L12 1 L12 4 L10.5 4 Z" fill-rule="evenodd"/></svg>
      <span>Monday to Friday: 4pm to 10PM<br>Saturday and Sundays: 10 AM to 5PM</span>
    </li>
  </ul>
</section>

<section class="card card--back">
  <svg class="card-bg" viewBox="0 0 929 532" preserveAspectRatio="none" aria-hidden="true">
    <path fill="var(--orange)" d="M15,532 C25,420 90,340 190,330 C300,320 380,380 480,375 C580,370 640,320 750,330 C850,340 905,430 910,532 Z"/>
  </svg>

  <p class="availability">NO APPOINTMENT NECESSARY</p>
  <div class="brand">
    <span class="brand-name">BAYFERN</span>
    <span class="brand-sub">URGENT CARE</span>
  </div>
  <p class="web-address">bayfernvet.com</p>
  <p class="tagline">WE'RE HERE WHEN YOU NEED US</p>
</section>

</body>
</html>
```